Buchcover-Design für psychologischen Ratgeber Morgens voller Mut!
Zielgruppe
Veröffentlichung psychologischer Ratgeber. Zielgruppe sind Erwachsene.
Aufgabenstellung
keine besondere Vorgaben, ein eyecatching-Cover wäre super. Der Titel des Buches lautet: Morgens voller Mut! Der Untertitel lautet: Heitere Seelenkunde für stille Kraft und Zuversicht
Autoren: Dr. Hanna Wiesmoor-Kalbach, Dr. Lukas Kalbach
Vielleicht macht es Sinn, einen Button mit: 199 Praxistipps auf dem Cover anzuführen.
Das Buch wird als Softcover und Ebook auf lesewelt veröffentlicht. Das Format ist 6 mal 9 Zoll und hat 425 Seiten.

```html
<!DOCTYPE html>
<html lang="de">
<head>
<meta charset="utf-8">
<title>Morgens voller Mut! – Buchcover</title>
<link rel="stylesheet" href="https://fonts.googleapis.com/css2?family=Rubik:wght@500;700;800;900&family=Roboto:wght@300&display=swap">
<style>
  :root{
    --navy:#0b2e79;
    --stripe-1:#2c68c8;
    --stripe-2:#3b7ad6;
    --stripe-3:#5592e4;
    --stripe-4:#6ca6ee;
    --stripe-5:#85b9f8;
    --title:#ffffff;
    --title-shadow:#4f86dc;
    --author:#b9d0f5;
    --subtitle:#58b45e;
    --body:#c9d8f3;
    --skin:rgba(226,176,150,.55);
    --hair:rgba(70,45,35,.45);
    --shirt:rgba(245,245,250,.5);
    --sky:#7ab2ec;
    --lilac:#9c86d8;
    --steel:#6f8fd0;
    --rose:#e88fc9;
    --sun:#f4b73d;
    --coral:#ef6f5c;
    --magenta:#e283c7;
    --azure:#6a9ee0;
    --leaf:#4fae5f;
    --violet:#9a7fd0;
    --pink:#ef87c7;
    --orange:#f2a23a;
    --ocean:#5b95e2;
    --periwinkle:#6b8fd8;
    --amethyst:#a683d4;
    --iris:#9180d4;
    --page:#f2f2f2;
  }
  *{box-sizing:border-box;margin:0;padding:0}
  html,body{width:698px;height:1200px;overflow:hidden;background:var(--page)}
  .canvas{position:relative;width:698px;height:1200px}

  .striped{
    background:linear-gradient(to bottom,
      var(--stripe-1) 0 36px, var(--stripe-2) 36px 70px, var(--stripe-3) 70px 104px,
      var(--stripe-4) 104px 138px, var(--stripe-5) 138px 170px,
      var(--navy) 170px 784px,
      var(--stripe-5) 784px 818px, var(--stripe-4) 818px 852px, var(--stripe-3) 852px 886px,
      var(--stripe-2) 886px 920px, var(--stripe-1) 920px 952px);
  }

  .spread{position:absolute;left:25px;top:24px;width:1361px;height:952px;
    transform:scale(0.4755);transform-origin:0 0}
  .cover-solo{position:absolute;left:142px;top:530px;width:628px;height:952px;
    transform:scale(0.66);transform-origin:0 0;box-shadow:0 18px 40px rgba(0,0,0,.25)}

  .tile{position:absolute;width:146px;height:146px;background-color:var(--tone)}
  .tile.tall{height:160px}
  .tile.plain{background:var(--tone)}
  .portrait{
    background-image:
      radial-gradient(ellipse 48% 26% at 50% 100%, var(--shirt) 0%, rgba(255,255,255,0) 100%),
      radial-gradient(ellipse 26% 34% at 50% 48%, var(--skin) 0%, rgba(0,0,0,0) 100%),
      radial-gradient(ellipse 36% 46% at 50% 46%, var(--hair) 0%, rgba(0,0,0,0) 100%),
      linear-gradient(160deg, rgba(255,255,255,.16), rgba(0,0,0,.08));
  }

  .back-copy{position:absolute;left:201px;top:219px;width:386px;
    font-family:"Roboto",sans-serif;font-weight:300;font-size:17.4px;line-height:27.2px;
    color:var(--body);text-align:justify;hyphens:manual;word-spacing:-0.3px}
  .back-copy p + p{margin-top:27px}

  .spine-title,.spine-authors{position:absolute;writing-mode:vertical-rl;white-space:nowrap}
  .spine-title{left:660px;top:228px;font-family:"Rubik",sans-serif;font-weight:900;
    font-size:35px;letter-spacing:1px;color:var(--title);text-shadow:3px 2px 0 var(--title-shadow)}
  .spine-authors{left:697px;top:238px;font-family:"Rubik",sans-serif;font-weight:700;
    font-size:11.5px;color:var(--author)}

  .front{position:absolute;left:733px;top:0;width:628px;height:952px}
  .cover-solo .front{left:0}

  .title{position:absolute;font-family:"Rubik",sans-serif;font-weight:900;color:var(--title);
    font-size:70px;line-height:1;letter-spacing:1px;text-transform:uppercase;white-space:nowrap;
    text-shadow:3px 3px 0 var(--title-shadow),6px 6px 10px rgba(0,0,0,.35)}
  .title-line-1{left:50px;top:338px}
  .title-line-2{left:108px;top:404px}
  .authors{position:absolute;left:430px;top:344px;font-family:"Rubik",sans-serif;font-weight:700;
    font-size:16px;line-height:18.5px;color:var(--author)}
  .subtitle{position:absolute;left:134px;top:487px;font-family:"Rubik",sans-serif;font-weight:700;
    font-size:26px;line-height:33px;color:var(--subtitle);text-transform:uppercase}
  .tips-badge{display:flex;flex-direction:column;align-items:center;justify-content:center;
    font-family:"Rubik",sans-serif;color:var(--title)}
  .tips-number{font-size:56px;font-weight:800;line-height:1}
  .tips-label{font-size:12px;font-weight:700;margin-top:2px;letter-spacing:.2px}
</style>
</head>
<body>
<div class="canvas">

  <!-- Flat wraparound: back, spine, front -->
  <div class="spread striped">
    <div class="back">
      <div class="tile portrait" style="left:22px;top:24px;--tone:var(--lilac)" role="img" aria-label="Porträtfoto: lachender junger Mann"></div>
      <div class="tile portrait" style="left:22px;top:170px;--tone:var(--sun)" role="img" aria-label="Porträtfoto: lächelnde rothaarige Frau"></div>
      <div class="tile tall plain" style="left:22px;top:316px;--tone:var(--leaf)"></div>
      <div class="tile portrait" style="left:22px;top:476px;--tone:var(--coral)" role="img" aria-label="Porträtfoto: lächelnde dunkelhaarige Frau"></div>
      <div class="tile portrait" style="left:22px;top:622px;--tone:var(--magenta)" role="img" aria-label="Porträtfoto: zwinkernde junge Frau"></div>
      <div class="tile tall plain" style="left:22px;top:768px;--tone:var(--periwinkle)"></div>

      <div class="back-copy">
        <p>Was gibt uns Mut? Das ist seit jeher eine Kernfrage des Menschen. Nach wissen&shy;schaftlichen Erkennt&shy;nissen der Heiteren Seelen&shy;kunde können wir durch bestimmte Gewohn&shy;heiten einen großen Teil unserer Zuver&shy;sicht selbst beein&shy;flussen. Auch und gerade in schwierigen Alltags&shy;situationen ist durch einfache psycho&shy;logische Übungen eine Stärkung der inneren Kraft und der Lebens&shy;freude möglich.</p>
        <p>Welche Gewohn&shy;heiten für ein mutiges Leben besonders förderlich sind, beschreiben die Autoren Dr. Hanna Wiesmoor-Kalbach, promovierte Psycho&shy;login, Psycho&shy;therapeutin sowie Lehr&shy;therapeutin für Verhaltens&shy;therapie, und Coach Dr. Lukas Kalbach anschaulich anhand von 199 Praxis&shy;tipps und Übungen. Zudem enthält das Buch 21 Tests und Frage&shy;bogen zur Selbst&shy;reflexion samt QR-Codes und Download&shy;links zum Ausdrucken.</p>
      </div>
    </div>

    <div class="spine-title">MORGENS VOLLER MUT!</div>
    <div class="spine-authors">Dr. Hanna Wiesmoor-Kalbach, Dr. Lukas Kalbach</div>

    <div class="front striped">
      <div class="tile portrait" style="left:19px;top:24px;--tone:var(--sky)" role="img" aria-label="Porträtfoto: lächelnde Frau"></div>
      <div class="tile portrait" style="left:165px;top:24px;--tone:var(--lilac)" role="img" aria-label="Porträtfoto: lachender junger Mann"></div>
      <div class="tile portrait" style="left:311px;top:24px;--tone:var(--steel)" role="img" aria-label="Porträtfoto: lachender Mann"></div>
      <div class="tile portrait" style="left:457px;top:24px;--tone:var(--rose)" role="img" aria-label="Porträtfoto: lachender Mann mit Bart"></div>
      <div class="tile portrait" style="left:19px;top:170px;--tone:var(--sun)" role="img" aria-label="Porträtfoto: lächelnde rothaarige Frau"></div>
      <div class="tile portrait" style="left:165px;top:170px;--tone:var(--coral)" role="img" aria-label="Porträtfoto: lächelnde dunkelhaarige Frau"></div>
      <div class="tile portrait" style="left:311px;top:170px;--tone:var(--magenta)" role="img" aria-label="Porträtfoto: zwinkernde Frau"></div>
      <div class="tile portrait" style="left:457px;top:170px;--tone:var(--azure)" role="img" aria-label="Porträtfoto: staunender junger Mann"></div>

      <div class="title title-line-1">Morgens</div>
      <div class="title title-line-2">voller Mut!</div>
      <div class="authors">Dr. Hanna<br>Wiesmoor-Kalbach,<br>Dr. Lukas Kalbach</div>
      <div class="subtitle">Heitere<br>Seelenkunde<br>für stille Kraft<br>und Zuversicht</div>

      <div class="tile portrait" style="left:457px;top:492px;--tone:var(--leaf)" role="img" aria-label="Porträtfoto: lächelnder junger Mann"></div>
      <div class="tile portrait" style="left:19px;top:638px;--tone:var(--violet)" role="img" aria-label="Porträtfoto: jubelnder Mann"></div>
      <div class="tile portrait" style="left:165px;top:638px;--tone:var(--pink)" role="img" aria-label="Porträtfoto: lächelnder junger Mann"></div>
      <div class="tile portrait" style="left:311px;top:638px;--tone:var(--orange)" role="img" aria-label="Porträtfoto: lächelnde Frau"></div>
      <div class="tile portrait" style="left:457px;top:638px;--tone:var(--ocean)" role="img" aria-label="Porträtfoto: lächelnde Frau mit Dutt"></div>
      <div class="tile portrait" style="left:19px;top:784px;--tone:var(--periwinkle)" role="img" aria-label="Porträtfoto: lächelnder Mann"></div>
      <div class="tile tips-badge" style="left:165px;top:784px;--tone:var(--amethyst)">
        <span class="tips-number">199</span><span class="tips-label">PRAXISTIPPS</span>
      </div>
      <div class="tile portrait" style="left:311px;top:784px;--tone:var(--leaf)" role="img" aria-label="Porträtfoto: lächelnde Frau"></div>
      <div class="tile portrait" style="left:457px;top:784px;--tone:var(--iris)" role="img" aria-label="Porträtfoto: lächelnder Mann mit Bart"></div>
    </div>
  </div>

  <!-- Flat front cover -->
  <div class="cover-solo">
    <div class="front striped">
      <div class="tile portrait" style="left:19px;top:24px;--tone:var(--sky)" role="img" aria-label="Porträtfoto: lächelnde Frau"></div>
      <div class="tile portrait" style="left:165px;top:24px;--tone:var(--lilac)" role="img" aria-label="Porträtfoto: lachender junger Mann"></div>
      <div class="tile portrait" style="left:311px;top:24px;--tone:var(--steel)" role="img" aria-label="Porträtfoto: lachender Mann"></div>
      <div class="tile portrait" style="left:457px;top:24px;--tone:var(--rose)" role="img" aria-label="Porträtfoto: lachender Mann mit Bart"></div>
      <div class="tile portrait" style="left:19px;top:170px;--tone:var(--sun)" role="img" aria-label="Porträtfoto: lächelnde rothaarige Frau"></div>
      <div class="tile portrait" style="left:165px;top:170px;--tone:var(--coral)" role="img" aria-label="Porträtfoto: lächelnde dunkelhaarige Frau"></div>
      <div class="tile portrait" style="left:311px;top:170px;--tone:var(--magenta)" role="img" aria-label="Porträtfoto: zwinkernde Frau"></div>
      <div class="tile portrait" style="left:457px;top:170px;--tone:var(--azure)" role="img" aria-label="Porträtfoto: staunender junger Mann"></div>

      <div class="title title-line-1">Morgens</div>
      <div class="title title-line-2">voller Mut!</div>
      <div class="authors">Dr. Hanna<br>Wiesmoor-Kalbach,<br>Dr. Lukas Kalbach</div>
      <div class="subtitle">Heitere<br>Seelenkunde<br>für stille Kraft<br>und Zuversicht</div>

      <div class="tile portrait" style="left:457px;top:492px;--tone:var(--leaf)" role="img" aria-label="Porträtfoto: lächelnder junger Mann"></div>
      <div class="tile portrait" style="left:19px;top:638px;--tone:var(--violet)" role="img" aria-label="Porträtfoto: jubelnder Mann"></div>
      <div class="tile portrait" style="left:165px;top:638px;--tone:var(--pink)" role="img" aria-label="Porträtfoto: lächelnder junger Mann"></div>
      <div class="tile portrait" style="left:311px;top:638px;--tone:var(--orange)" role="img" aria-label="Porträtfoto: lächelnde Frau"></div>
      <div class="tile portrait" style="left:457px;top:638px;--tone:var(--ocean)" role="img" aria-label="Porträtfoto: lächelnde Frau mit Dutt"></div>
      <div class="tile portrait" style="left:19px;top:784px;--tone:var(--periwinkle)" role="img" aria-label="Porträtfoto: lächelnder Mann"></div>
      <div class="tile tips-badge" style="left:165px;top:784px;--tone:var(--amethyst)">
        <span class="tips-number">199</span><span class="tips-label">PRAXISTIPPS</span>
      </div>
      <div class="tile portrait" style="left:311px;top:784px;--tone:var(--leaf)" role="img" aria-label="Porträtfoto: lächelnde Frau"></div>
      <div class="tile portrait" style="left:457px;top:784px;--tone:var(--iris)" role="img" aria-label="Porträtfoto: lächelnder Mann mit Bart"></div>
    </div>
  </div>

</div>
</body>
</html>
```